依頼詳細
富山県高岡市「緑ヶ丘市議会」で、明協系会派「明政協和党緑ヶ丘市議会議員会」を結成し、活動を行ってきましたが、それを市民の皆さんにお伝えするために、会報誌を発行したくコンペ方式でデザインをお願いするものです。
宜しくお願い致します。
記載項目
明政協和党緑ヶ丘市議会議員会/090-2846-3917(政調会長森下)/作成料5~10万円
サイズ
B4
ページ数
両面
希望イメージ
シンプル 複雑
単色 カラフル
暗い 明るい
日常 高級
遊び心 厳粛
未来的 伝統的
女性的 男性的
希望する色
赤系、緑系、黄・オレンジ系
納品ファイル
• イラストレーター形式 (.ai)
補足説明
・非常に急いでいます
・ロゴは下記からダウンロードお願いします(ただし、党の広報誌でなく、議会会派の広報誌なので控えめでお願いします)
https://www.sakura-meikyo.jp/policy-koho
https://www.sakura-meikyo.jp/introduction2/pdf/logo_type_A.JPG
デザイン案の提示を使用にも情報が不足しているとのご指摘・ご質問を頂きました。

そこで、掲載する内容(タイトル、文章、写真及びキャプション)を1つのWordデータにまとめました。
また、当方において、手書きで記載したレイアウト案図(表面及び裏面)データ2点を合わせて送付します。

なお、デザインの良さと価格を見て採用を決めたいと思いますので、
その点も踏まえてご提案を宜しくお願いします。
本件は12月10日(木)に開始するも、情報が不足しているとのご意見・ご指摘を受けました。
そこで、12月13日(日)夜中に、掲載頂きたい情報(文章や写真及びキャプションなど)を追記したところです。

今般、当該内容について、少しだけ修正を加えました。
修正箇所は分かりやすいように黄色に着色又は黄色の枠で囲ってありますので、ご確認の上、既に提出の方は修正対応頂ければ幸いに存じます。
未提出の方は、今回のデータを元にデザイン案を作成願います。

なお、仮に修正対応されなかったとしても、レイアウトの案をご提示いただいていますので、それでもって、私たちの会派の政務調査会を開催し、採用デザイン案を週明け12月22日(月)に決定する予定です。

以上、宜しくお願い致します。
■ 選んだ理由

シンプルで明瞭なデザイン、色使いで、パッと見て目につきやすい印象を受けました。
今回の私たちの目的が、多くの市民の皆さまにご覧頂くことであり、その観点から一番最適であると判断した次第です。

■ 提案者全員のお礼・コメント

年末の依頼で、皆さまお忙しい中、多くのご提案を頂きました。
そして提案のどれもが、非常に質が高く、驚きと感動をもって全提案を拝見させて頂きました。
残念ながら、選定できるのは1点であり、選定できなかった皆さま方には誠に申し訳ございません。

なお、今回初の会派広報紙の発行、そしてクリエモールの活用であり、今後もし仕事を依頼することがありましたら、その際にはぜひご協力頂ければ幸いに存じます。

皆さまのご健康とご多幸、そして良い年を迎えられるよう祈念申し上げ御礼のコメントとします。
誠にありがとうございました。

```html
<!DOCTYPE html>
<html lang="ja">
<head>
<meta charset="utf-8">
<title>明政協和党緑ヶ丘市議会議員会 活動報告 Vol.1</title>
<link rel="stylesheet" href="https://fonts.googleapis.com/css2?family=Noto+Sans+JP:wght@400;500;700;900&family=Montserrat:wght@700;800&display=swap">
<style>
  :root{
    --green:#2e8b3e;
    --green-dark:#1d5b35;
    --green-soft:#e4f1e3;
    --orange:#f29a1a;
    --ink:#222;
    --ink-soft:#555;
    --paper:#ffffff;
  }
  *{box-sizing:border-box;margin:0;padding:0}
  html,body{width:846px;height:1200px;overflow:hidden;background:var(--paper)}
  body{font-family:"Noto Sans JP",sans-serif;color:var(--ink);position:relative}

  .masthead{position:absolute;left:56px;top:22px;width:640px}
  .masthead__council{font-size:24px;font-weight:700;letter-spacing:.04em;line-height:1.3}
  .masthead__title{font-size:40px;font-weight:900;letter-spacing:-.01em;margin-left:-14px;line-height:1.2}
  .masthead__sub{font-size:26px;font-weight:700;margin-left:200px;letter-spacing:.08em;line-height:1.3;margin-top:2px}

  .issue-badge{position:absolute;right:40px;top:26px;width:96px;height:96px;border-radius:50%;
    background:var(--green);color:#fff;text-align:center;display:flex;flex-direction:column;justify-content:center}
  .issue-badge__label{font-family:"Montserrat",sans-serif;font-size:12px;font-weight:700;line-height:1.1}
  .issue-badge__vol{font-family:"Montserrat",sans-serif;font-size:28px;font-weight:800;line-height:1.1}

  .hero{position:absolute;left:0;top:160px;width:846px;height:250px}
  .hero__photo{position:absolute;inset:0}
  .hero__figure{position:absolute;right:36px;top:150px;width:90px;height:112px;border-radius:45px 45px 30px 30px;
    background:linear-gradient(#ffffff,#e6eef5);box-shadow:0 0 0 1px #dde6ee}

  .section-lead{position:absolute;left:70px;top:418px;width:640px}
  .section-lead__heading{color:var(--green);font-size:23px;font-weight:900;border-bottom:2px solid var(--green);
    padding-bottom:4px;display:inline-block;margin-left:130px;line-height:1.4}
  .section-lead__text{font-size:12.5px;line-height:1.7;color:var(--ink-soft);margin-top:8px;padding-left:40px}

  .members{position:absolute;left:40px;top:566px;width:766px}
  .members__label{display:inline-block;background:var(--green);color:#fff;font-size:15px;font-weight:700;
    padding:2px 18px;border-radius:14px;line-height:1.5}
  .members__row{display:flex;justify-content:space-between;margin-top:10px;padding:0 10px}
  .member{width:80px;text-align:center}
  .member__portrait{width:68px;height:68px;border-radius:50%;margin:0 auto;
    background:linear-gradient(#d9dde3,#8a929c);border:2px solid #fff;box-shadow:0 0 0 1px #ccc}
  .member__name{font-size:10px;margin-top:4px;line-height:1.25;color:var(--ink-soft)}
  .member__name b{display:block;font-size:12px;color:var(--ink);font-weight:700}

  .activities-band{position:absolute;left:40px;top:846px;width:766px;height:48px;background:var(--green-dark);
    color:#fff;font-size:22px;font-weight:900;display:flex;align-items:center;padding-left:24px;border-radius:4px}
  .activities-band em{font-style:normal;color:var(--orange);font-size:26px;margin:0 2px}

  .activities{position:absolute;left:56px;top:910px;width:740px;display:flex;gap:16px}
  .activities__photo{width:212px;height:140px;background:linear-gradient(135deg,#c9b9a2,#6b5d4f);border-radius:2px}
  .activities__list{list-style:none;flex:1;border:1.5px solid var(--green);border-radius:4px;padding:10px 14px;background:var(--green-soft)}
  .activities__list li{font-size:12.5px;font-weight:500;line-height:1.72;white-space:nowrap;overflow:hidden}
</style>
</head>
<body>

<header class="masthead">
  <p class="masthead__council">緑ヶ丘市議会</p>
  <h1 class="masthead__title">「明政協和党緑ヶ丘市議会議員会」</h1>
  <p class="masthead__sub">活動報告</p>
</header>

<div class="issue-badge">
  <span class="issue-badge__label">News Letter</span>
  <span class="issue-badge__vol">Vol.1</span>
</div>

<section class="hero">
  <svg class="hero__photo" viewBox="0 0 846 250" width="846" height="250" role="img" aria-label="海岸の岩と松のある冬の海景写真">
    <defs>
      <linearGradient id="sea" x1="0" y1="0" x2="0" y2="1">
        <stop offset="0" stop-color="#a9d6f2"/>
        <stop offset=".55" stop-color="#5aa3d3"/>
        <stop offset="1" stop-color="#2c6f9e"/>
      </linearGradient>
    </defs>
    <path d="M40 0 H806 V205 Q600 250 420 228 Q220 205 40 240 Z" fill="url(#sea)"/>
  </svg>
  <div class="hero__figure" role="img" aria-label="雪だるまのイラスト"></div>
</section>

<section class="section-lead">
  <h2 class="section-lead__heading">市議会、そして会派の活動・役割について</h2>
  <p class="section-lead__text">
    市の運営に必要な予算、あるいは市民の義務を規定するなどの条例は、<br>
    全て議会において市議会の承認を得た上で、決定・実施されます。<br>
    会派では、市当局に対して要望書を提出し、市議会の各委員会での質疑や調査研究を通じて、<br>
    市民の皆様に寄り添った施策の実現に向けて活動を続けてまいります。
  </p>
</section>

<section class="members">
  <span class="members__label">会派構成員紹介</span>
  <div class="members__row">
    <div class="member"><div class="member__portrait" role="img" aria-label="議員の顔写真"></div><p class="member__name">会長<b>青山 誠一</b></p></div>
    <div class="member"><div class="member__portrait" role="img" aria-label="議員の顔写真"></div><p class="member__name">幹事長<b>石川 健二</b></p></div>
    <div class="member"><div class="member__portrait" role="img" aria-label="議員の顔写真"></div><p class="member__name">政調会長<b>森下 浩一</b></p></div>
    <div class="member"><div class="member__portrait" role="img" aria-label="議員の顔写真"></div><p class="member__name">総務会長<b>上野 隆</b></p></div>
    <div class="member"><div class="member__portrait" role="img" aria-label="議員の顔写真"></div><p class="member__name">副議長<b>岡本 修</b></p></div>
    <div class="member"><div class="member__portrait" role="img" aria-label="議員の顔写真"></div><p class="member__name">議員<b>川村 聡</b></p></div>
    <div class="member"><div class="member__portrait" role="img" aria-label="議員の顔写真"></div><p class="member__name">議員<b>北原 正</b></p></div>
    <div class="member"><div class="member__portrait" role="img" aria-label="議員の顔写真"></div><p class="member__name">議員<b>小島 恵子</b></p></div>
  </div>
  <div class="members__row">
    <div class="member"><div class="member__portrait" role="img" aria-label="議員の顔写真"></div><p class="member__name">議員<b>佐野 一郎</b></p></div>
    <div class="member"><div class="member__portrait" role="img" aria-label="議員の顔写真"></div><p class="member__name">議員<b>杉本 大輔</b></p></div>
    <div class="member"><div class="member__portrait" role="img" aria-label="議員の顔写真"></div><p class="member__name">議員<b>高田 明</b></p></div>
    <div class="member"><div class="member__portrait" role="img" aria-label="議員の顔写真"></div><p class="member__name">議員<b>中井 昭彦</b></p></div>
    <div class="member"><div class="member__portrait" role="img" aria-label="議員の顔写真"></div><p class="member__name">議員<b>野村 茂</b></p></div>
    <div class="member"><div class="member__portrait" role="img" aria-label="議員の顔写真"></div><p class="member__name">議員<b>平田 博</b></p></div>
    <div class="member"><div class="member__portrait" role="img" aria-label="議員の顔写真"></div><p class="member__name">議員<b>村井 直子</b></p></div>
  </div>
</section>

<div class="activities-band">結成から1年、これまでの<em>私たちの</em>主な活動について</div>

<section class="activities">
  <div class="activities__photo" role="img" aria-label="会派の要望書提出の様子の写真"></div>
  <ol class="activities__list">
    <li>(1) 危機への迅速な対応「感染症対策」に係る要望及び質問</li>
    <li>(2) 副議長を中心に市役所本庁舎の整備計画を審査・提言</li>
    <li>(3) 市制施行記念の行事に向けた議会運営の改善を提言</li>
    <li>(4) 議会改革を推進し、議員定数と報酬の見直しに着手</li>
    <li>(5) 政策集を作成し、政策実現に向けた要望書を提出</li>
    <li>(6) 政策研修会を開催し「会派の政策」を取りまとめ</li>
  </ol>
</section>

</body>
</html>
```